Equipment Finance Specialist I work with companies who need the funds to buy their equipment

I would like a business card that stands out on the shelves. I want to be able to hand it to someone and say WOW. This card should have my logo.
You can put color into it I am very open on design and color

What my company does is we deal with dealerships that sell equipment such as Dump Trucks garbage trucks tractors trailers. Customers get referred to us and depending on their time in business we will ask for the following items

Companies that have been in business for more than two years we have a credit application program up to 250K . With this program we need the following items Credit application filled out(which is what I would like to be able for the customer to click on my website to get.) as well as three current month bank statements.

Deals over 250k we will need the following items

2 years business tax returns
2 years personal tax returns
Profit & Loss statement
Personal Financial Statement

what we do
100% FINANCING
SEASONAL PAYMENTS
LOAN BALLOON PAYMENTS
TRAC LEASING
LOW-INTEREST REFINANCING RATES
DEBT CONSOLIDATION

We specialize in creative financing solutions and offer a variety of reliable, flexible and expandable lending choices.

Target Market(s)

Trucking Companies

Industry/Entity Type

Trucking Company

Contact Information for Business Card

* $250,000 Application only Program
* Loans from $30,000 to 5,000,000
* Competitive Interest Rates

Font styles to use
Serif
Sans Serif

Colors

Designer to choose colors to be used in the design.

Requirements
Must have
• On the back of the card.
• * $250,000 Application only Program
• * Loans from $30,000 to 5,000,000
• My name, email, website. address
• * Competitive Interest Rates
• * 100% Financing
Nice to have
• I want my logo to pop on the card
• My logo is the great one I would like to use
Should not have
• I am up for your creativity as well

```html
<!DOCTYPE html>
<html lang="en">
<head>
<meta charset="utf-8">
<title>Ridgeline Capital – Business Card</title>
<link href="https://fonts.googleapis.com/css2?family=Open+Sans:wght@400;600;700&family=Oswald:wght@400;500&display=swap" rel="stylesheet">
<style>
  :root{
    --backdrop:#2b2b2d;
    --paper:#f7f7f7;
    --navy:#0f2a6b;
    --band:#16307a;
    --red:#d0102e;
    --grey:#3d3d3d;
    --rule:#b9b9b9;
    --ink:#111214;
    --ink-2:#26272a;
    --light:#f2f2f2;
  }
  *{box-sizing:border-box;margin:0;padding:0}
  html,body{width:1200px;height:900px;overflow:hidden}
  body{background:var(--backdrop);font-family:"Open Sans",Arial,sans-serif;position:relative}

  .card{position:absolute;left:320px;width:560px;height:320px;overflow:hidden;box-shadow:0 10px 24px rgba(0,0,0,.45)}
  .card::after{content:"";position:absolute;left:0;right:0;bottom:0;height:10px;background:var(--band)}

  /* front */
  .card--front{top:80px;background:var(--paper);text-align:center}
  .brand{display:flex;align-items:center;justify-content:center;gap:12px;margin-top:40px}
  .brand__dot{width:34px;height:34px;border-radius:50%;background:var(--navy)}
  .brand__name{font-weight:700;font-size:38px;color:var(--navy);letter-spacing:1px;text-transform:uppercase}
  .requirements{margin-top:16px;color:var(--navy);font-size:15.5px;line-height:1.35}
  .requirements .sep{margin:0 6px}
  .rule{height:1px;background:var(--rule);margin:12px 34px 0}
  .section-title{margin-top:10px;color:var(--navy);font-weight:700;font-size:13px}
  .services{margin-top:6px;color:var(--grey);font-size:12.5px;line-height:1.6;text-transform:uppercase}
  .bullet{display:inline-block;width:6px;height:6px;border-radius:50%;background:var(--red);margin:0 9px 2px;vertical-align:middle}

  /* back */
  .card--back{top:480px;background:linear-gradient(135deg,var(--ink-2),var(--ink) 70%);color:var(--light)}
  .person{position:absolute;left:52px;top:58px}
  .person__name{font-family:"Oswald",Arial Narrow,sans-serif;font-weight:500;font-size:27px;color:var(--red);text-transform:uppercase;line-height:1.1}
  .person__role{font-size:14px;margin-left:34px}
  .contacts{position:absolute;left:300px;top:80px;list-style:none;font-size:15.5px;line-height:1.5}
  .contacts li{display:flex;align-items:center;gap:6px}
  .contacts svg{width:12px;height:12px;fill:var(--red);flex:none}
  .address{position:absolute;left:150px;top:160px;font-size:15.5px}
  .back-rule{position:absolute;left:42px;right:42px;top:196px;height:1px;background:#6b6b6b}
  .offers{position:absolute;top:210px;list-style:none;font-size:15.5px;line-height:1.35}
  .offers--left{left:42px}
  .offers--right{left:300px;top:236px}
  .offers li::before{content:"";display:inline-block;width:6px;height:6px;border-radius:50%;background:var(--red);margin-right:7px;vertical-align:middle}
</style>
</head>
<body>

<section class="card card--front">
  <div class="brand">
    <span class="brand__dot"></span>
    <span class="brand__name">Ridgeline Capital</span>
  </div>
  <p class="requirements">
    2 years business tax returns<span class="sep">|</span>2 years personal tax returns<br>
    Profit &amp; Loss statement<span class="sep">|</span>Personal Financial Statement
  </p>
  <div class="rule"></div>
  <h2 class="section-title">WHAT WE DO</h2>
  <p class="services">
    100% Financing<span class="bullet"></span>Seasonal Payments<span class="bullet"></span>Loan Balloon Payments<br>
    TRAC Leasing<span class="bullet"></span>Low-Interest Refinancing Rates<span class="bullet"></span>Debt Consolidation
  </p>
</section>

<section class="card card--back">
  <div class="person">
    <h1 class="person__name">Marcus Hale</h1>
    <p class="person__role">Managing Director</p>
  </div>
  <ul class="contacts">
    <li><svg viewBox="0 0 24 24"><path d="M6.6 10.8a15.1 15.1 0 0 0 6.6 6.6l2.2-2.2c.3-.3.7-.4 1-.2 1.1.4 2.3.6 3.6.6.6 0 1 .4 1 1V20c0 .6-.4 1-1 1A17 17 0 0 1 3 4c0-.6.4-1 1-1h3.5c.6 0 1 .4 1 1 0 1.3.2 2.5.6 3.6.1.3 0 .7-.2 1z"/></svg>055-210 884 316</li>
    <li><svg viewBox="0 0 24 24"><path d="M2 5h20v14H2zm2 2v.5l8 5 8-5V7l-8 5z"/></svg>hello@ridgelinecap.com</li>
    <li><svg viewBox="0 0 24 24"><circle cx="12" cy="12" r="10"/></svg>www.ridgelinecap.com</li>
  </ul>
  <p class="address">88, Harbor Road, 30719, Eastland</p>
  <div class="back-rule"></div>
  <ul class="offers offers--left">
    <li>$250,000 Application only Program</li>
    <li>Loans from $30,000 to 5,000,000</li>
  </ul>
  <ul class="offers offers--right">
    <li>Competitive Interest Rates</li>
    <li>100% Financing</li>
  </ul>
</section>

</body>
</html>
```